High end building company who specialise in architecturally designed homes needing a presentation do

We need a document/template that can be used in Indesign. We present proposal's, house plans, specifications at various stages throughout a building project from initial contact right through to completion. We want to have the same feel through out each presentation and be able to use the same first few pages and then be able to insert the contents. Sometimes the content will be A4 and other times when presenting plans will be A3. I have attached an example of one previously used for presenting plans (see 01_Conceptual) and one for proposals (see Proposal Example ). The document needs to have a minimalist look and feel very sophisticated to suit our client base. The look of the document should tie in with our logo design which is also attached.

It Company

```html
<!DOCTYPE html>
<html lang="en">
<head>
<meta charset="utf-8">
<title>Project Proposal – Marlow Keane Constructions</title>
<link rel="stylesheet" href="https://fonts.googleapis.com/css2?family=Oswald:wght@400;500;600&family=Raleway:wght@400;500&display=swap">
<style>
  :root {
    --backdrop: #a0a0a0;
    --charcoal: #3e3e40;
    --charcoal-deep: #333335;
    --paper: #ededed;
    --orange: #e8641f;
    --orange-bright: #f06a22;
    --peach: #f3c8ae;
    --ink: #2f2f31;
    --white: #ffffff;
    --title-light: #f1e5dc;
  }
  html, body {
    margin: 0;
    padding: 0;
    width: 883px;
    height: 1200px;
    overflow: hidden;
    background: var(--backdrop);
  }
  .canvas {
    position: relative;
    width: 883px;
    height: 1200px;
  }
  .spread {
    position: absolute;
    left: 87px;
    width: 709px;
    display: block;
  }
  .spread--cover { top: 90px; height: 500px; }
  .spread--mission { top: 610px; height: 501px; }
  .cover-title { font-family: "Oswald", sans-serif; font-weight: 500; }
  .brand-name { font-family: "Oswald", sans-serif; font-weight: 400; letter-spacing: 3px; }
  .web-address { font-family: "Oswald", sans-serif; font-weight: 400; letter-spacing: 4.5px; }
  .contact-block { font-family: "Oswald", sans-serif; font-weight: 400; }
  .mission-heading { font-family: "Oswald", sans-serif; font-weight: 500; }
  .mission-body { font-family: "Raleway", sans-serif; font-weight: 400; }
</style>
</head>
<body>
<main class="canvas">

  <!-- Cover spread -->
  <svg class="spread spread--cover" viewBox="0 0 886 625" xmlns="http://www.w3.org/2000/svg">
    <defs>
      <clipPath id="front-page"><rect x="443" y="0" width="443" height="625"/></clipPath>
      <linearGradient id="site-sky" x1="0" y1="0" x2="0" y2="1">
        <stop offset="0" stop-color="#5d86b8"/>
        <stop offset="0.55" stop-color="#a9b4b8"/>
        <stop offset="1" stop-color="#c7c19a"/>
      </linearGradient>
      <linearGradient id="orange-wash" x1="0" y1="0" x2="1" y2="1">
        <stop offset="0" stop-color="#e0621f"/>
        <stop offset="1" stop-color="#f26f22"/>
      </linearGradient>
    </defs>

    <!-- back cover -->
    <rect class="back-cover" x="0" y="0" width="443" height="625" fill="var(--charcoal)"/>
    <path class="back-cover-footer" d="M0 526 H130 L134 518 H310 L314 526 H443 V625 H0 Z" fill="var(--charcoal-deep)"/>
    <g class="contact-block" text-anchor="middle">
      <text x="221" y="560" font-size="7.5" fill="var(--orange)">Business Contacts:</text>
      <text x="221" y="571" font-size="7.5" fill="var(--white)">+49 (30) 512 447 208</text>
      <text x="221" y="582" font-size="7.5" fill="var(--white)">office@marlowkeane.com</text>
      <text x="221" y="593" font-size="7.5" fill="var(--white)">www.marlowkeane.com</text>
    </g>

    <!-- front cover -->
    <rect class="front-cover" x="443" y="0" width="443" height="625" fill="var(--paper)"/>
    <g clip-path="url(#front-page)">
      <path class="orange-field" d="M443 283 L549 177 Q555 171 561 177 L886 502 V625 H443 Z" fill="url(#orange-wash)"/>
      <rect class="accent-diamond" x="476" y="129" width="54" height="54" rx="7" transform="rotate(45 503 156)" fill="var(--orange)"/>
      <rect class="accent-diamond" x="831" y="222" width="32" height="32" rx="5" transform="rotate(45 847 238)" fill="var(--orange)"/>
      <g role="img" aria-label="Photo of glass towers and construction workers in hard hats on a building site">
        <rect x="693" y="-15" width="166" height="166" rx="8" transform="rotate(45 776 68)" fill="url(#site-sky)"/>
        <rect x="593" y="108" width="96" height="96" rx="8" transform="rotate(45 641 156)" fill="url(#site-sky)"/>
        <rect x="676" y="195" width="96" height="96" rx="8" transform="rotate(45 724 243)" fill="url(#site-sky)"/>
      </g>
    </g>

    <g class="brand">
      <circle cx="486" cy="56" r="18" fill="var(--ink)"/>
      <text class="brand-name" x="512" y="47" font-size="11" fill="var(--ink)">MARLOW</text>
      <text class="brand-name" x="512" y="60" font-size="11" fill="var(--ink)">KEANE</text>
      <text class="brand-name" x="512" y="73" font-size="11" fill="var(--ink)">CONSTRUCTIONS</text>
    </g>

    <g class="cover-title">
      <text x="501" y="396" font-size="44" fill="var(--title-light)">PROJECT</text>
      <text x="501" y="444" font-size="44" fill="var(--ink)">PROPOSAL</text>
      <text x="501" y="482" font-size="35" fill="var(--title-light)">SEASIDE</text>
      <text x="501" y="522" font-size="35" fill="var(--title-light)">DRIVE</text>
      <text x="501" y="563" font-size="35" fill="var(--title-light)">HOUSE</text>
    </g>

    <path class="web-band" d="M631 625 L671 585 H886 V625 Z" fill="var(--charcoal)"/>
    <text class="web-address" x="689" y="611" font-size="13" fill="var(--white)">harrowandfield.com</text>
  </svg>

  <!-- Mission spread -->
  <svg class="spread spread--mission" viewBox="0 0 886 626" xmlns="http://www.w3.org/2000/svg">
    <defs>
      <clipPath id="mission-page"><rect x="0" y="0" width="886" height="626"/></clipPath>
      <radialGradient id="hands-photo" cx="0.35" cy="0.55" r="0.8">
        <stop offset="0" stop-color="#8a8785"/>
        <stop offset="0.45" stop-color="#b3afab"/>
        <stop offset="1" stop-color="#d9d6d3"/>
      </radialGradient>
    </defs>
    <g clip-path="url(#mission-page)">
      <rect role="img" aria-label="Black and white photo of cupped hands holding a small bonsai tree" x="0" y="0" width="886" height="626" fill="url(#hands-photo)"/>
      <rect class="fold-tint" x="443" y="0" width="443" height="626" fill="var(--white)" opacity="0.12"/>
      <path class="mission-shape" d="M434 0 H886 V273 L802 351 Q796 357 790 351 Z" fill="var(--orange-bright)" opacity="0.95"/>
      <path class="soft-diamond" d="M555 626 L796 385 L886 475 V626 Z" fill="var(--white)" opacity="0.22"/>
      <rect class="peach-diamond" x="645" y="317" width="108" height="108" rx="10" transform="rotate(45 699 371)" fill="var(--peach)" opacity="0.85"/>
      <rect class="peach-diamond" x="825" y="345" width="52" height="52" rx="7" transform="rotate(45 851 371)" fill="var(--peach)" opacity="0.85"/>
    </g>

    <text class="mission-heading" x="826" y="74" font-size="16" text-anchor="end" fill="var(--white)">OUR MISSION</text>
    <rect class="mission-rule" x="789" y="82" width="37" height="2.5" fill="var(--white)"/>
    <g class="mission-body" font-size="7.6" fill="var(--white)" text-anchor="end">
      <text x="826" y="97">is to design and develop lasting,</text>
      <text x="826" y="108">impactful, iconic external</text>
      <text x="826" y="119">environments. Our aim is to create a</text>
      <text x="826" y="129">sense of place, embrace local</text>
      <text x="826" y="140">culture and lifestyles, and forge a</text>
      <text x="826" y="151">sustainable legacy. We want to</text>
      <text x="826" y="161">enrich everyday life, and see people</text>
      <text x="826" y="172">interact with and enjoy the external</text>
      <text x="826" y="183">environments we create.</text>
    </g>
  </svg>

</main>
</body>
</html>
```